Harborlight Willow Home Care Business Cards

We are looking to create double sided, sleek business cards for our new Home Health Care Agency, Harborlight Willow Home Care, located in NJ. We want to appear established, professional and at the same time, stand out with a creative and original flair. It should have a luxurious, exclusive feel to it.
The theme colors from our logo should be incorporated into the project.

Our Logo is attached.

Information to be included on the business cards:

Insert Phone Icon: (555)-204-7390
Insert Website Icon: hwhcpx.example
Insert E-mail Icon: info@hwhcpx.example

Follow us on Social Media!
Insert Facebook Icon: (I will provide the link at a later time)
Insert Instagram Icon (I will provide the link at a later time)

In regard to location, we service the areas of: Bayville
Cedarwood
Flint
Dale
Hollis
Gull Heights
Jarvis
Lakemoor
Linwick
Marlow Township
Point Willow Beach
Rowanfield
Long Reach
Tern River

All all it's neighboring areas.

However, that can take up a lot of room...therefore, I had in mind to use the backside of the card to have a MAP with all these areas marked on there...in addition to listing these service locations below the map.

We want the card to appear lively and vibrant.

Please note: I will provide the potential winner with the contact's name later on in the process.

A sample idea is attached below as well.

Use your creative juices!

Good luck!

• A map of our service areas on the back of the double sided card.
Sleek design
Our logo (refer to attachment below)

```html
<!DOCTYPE html>
<html lang="en">
<head>
<meta charset="utf-8">
<title>Harborlight Willow Home Care – Business Cards</title>
<link rel="stylesheet" href="https://fonts.googleapis.com/css2?family=Montserrat:wght@600;700&family=Open+Sans:wght@400;600&display=swap">
<style>
  :root {
    --brand-blue: #0c58a3;
    --brand-green: #7cc242;
    --paper: #ffffff;
    --backdrop: #e9eaec;
    --text-light: #e9f0f8;
  }
  * { margin: 0; padding: 0; box-sizing: border-box; }
  html, body { width: 1200px; height: 873px; overflow: hidden; }
  body {
    background: var(--backdrop);
    font-family: "Open Sans", Arial, sans-serif;
    position: relative;
  }
  .card {
    position: absolute;
    overflow: hidden;
    box-shadow: 0 6px 18px rgba(0,0,0,.18);
  }

  /* Front */
  .card--front {
    left: 110px; top: 139px;
    width: 340px; height: 595px;
    background: var(--brand-blue);
  }
  .front__top {
    height: 262px;
    background: var(--paper);
    border-bottom: 5px solid var(--brand-green);
    display: flex; align-items: center; justify-content: center;
    padding: 0 26px;
  }
  .brand {
    display: flex; align-items: center; gap: 10px;
    font-family: "Montserrat", Arial, sans-serif;
    font-weight: 700;
    text-transform: uppercase;
    line-height: 1.15;
  }
  .brand__dot {
    flex: none;
    width: 34px; height: 34px; border-radius: 50%;
    background: var(--brand-green);
  }
  .brand--front { color: var(--brand-blue); font-size: 17px; }
  .brand--back { color: var(--paper); font-size: 22px; }

  .front__body { padding: 40px 0 0 44px; color: var(--text-light); }
  .person__name {
    font-family: "Montserrat", Arial, sans-serif;
    font-weight: 700; font-size: 22px; letter-spacing: .5px;
    color: var(--brand-green);
  }
  .person__title { font-size: 17px; margin-top: 2px; }
  .divider {
    width: 24px; height: 3px; background: var(--brand-green);
    margin: 22px 0 18px;
  }
  .contact { list-style: none; }
  .contact li {
    display: flex; align-items: center; gap: 12px;
    font-size: 17px; height: 31px;
  }
  .contact__icon {
    flex: none; width: 18px; height: 18px;
    display: flex; align-items: center; justify-content: center;
  }
  .contact__icon--square { background: var(--brand-green); border-radius: 2px; }

  /* Back */
  .card--back {
    left: 520px; top: 266px;
    width: 595px; height: 340px;
    background: var(--brand-blue);
    padding: 70px 0 0 0;
  }
  .back__brand { display: flex; justify-content: center; }
  .back__rule {
    width: 300px; height: 2px; background: var(--brand-green);
    margin: 14px auto 40px;
  }
  .areas {
    list-style: none;
    color: var(--text-light);
    font-size: 14px;
    text-align: center;
    line-height: 1.8;
    padding: 0 30px;
  }
  .areas span { white-space: nowrap; }
  .areas span::before {
    content: "";
    display: inline-block; width: 7px; height: 7px; border-radius: 50%;
    background: var(--brand-green);
    margin: 0 6px 2px 8px;
  }
</style>
</head>
<body>

<section class="card card--front" aria-label="Business card front">
  <div class="front__top">
    <div class="brand brand--front"><span class="brand__dot"></span>Harborlight Willow Home Care</div>
  </div>
  <div class="front__body">
    <h1 class="person__name">MARCUS ELLERY</h1>
    <p class="person__title">Managing Director</p>
    <div class="divider"></div>
    <ul class="contact">
      <li>
        <span class="contact__icon">
          <svg width="18" height="18" viewBox="0 0 24 24" aria-hidden="true"><path fill="#7cc242" d="M6.6 10.8a15.1 15.1 0 0 0 6.6 6.6l2.2-2.2a1 1 0 0 1 1-.25 11.4 11.4 0 0 0 3.6.57 1 1 0 0 1 1 1V20a1 1 0 0 1-1 1A17 17 0 0 1 3 4a1 1 0 0 1 1-1h3.5a1 1 0 0 1 1 1c0 1.25.2 2.45.57 3.57a1 1 0 0 1-.25 1z"/></svg>
        </span>(555)-204-7390
      </li>
      <li>
        <span class="contact__icon">
          <svg width="18" height="14" viewBox="0 0 18 14" aria-hidden="true"><rect width="18" height="14" rx="1" fill="#7cc242"/><path d="M1 1.5l8 6 8-6" fill="none" stroke="#0c58a3" stroke-width="1.6"/></svg>
        </span>info@hwhcpx.example
      </li>
      <li>
        <span class="contact__icon">
          <svg width="18" height="18" viewBox="0 0 18 18" aria-hidden="true"><circle cx="9" cy="9" r="8" fill="#7cc242"/><path d="M1 9h16M9 1c-3 3.5-3 12.5 0 16M9 1c3 3.5 3 12.5 0 16" fill="none" stroke="#0c58a3" stroke-width="1.2"/></svg>
        </span>www.hwhcpx.example
      </li>
      <li><span class="contact__icon contact__icon--square"></span>@hwhcpx</li>
      <li><span class="contact__icon contact__icon--square"></span>@hwhcpx</li>
    </ul>
  </div>
</section>

<section class="card card--back" aria-label="Business card back">
  <div class="back__brand">
    <div class="brand brand--back"><span class="brand__dot"></span>Harborlight Willow Home Care</div>
  </div>
  <div class="back__rule"></div>
  <ul class="areas">
    <li><span>Cedarwood</span><span>Flint</span><span>Dale</span><span>Hollis</span><span>Gull Heights</span><span>Jarvis</span></li>
    <li><span>Lakemoor</span><span>Linwick</span><span>Marlow Township</span><span>Point Willow Beach</span></li>
    <li><span>Rowanfield</span><span>Long Reach</span><span>Tern River</span></li>
  </ul>
</section>

</body>
</html>
```